Criação de Cardápio para Beleza
" O Salão fica em uma casa de 02 andares, sendo que no primeiro é um grande salão onde funcionam atividades voltadas à beleza feminina e masculina (manicure, corte de cabelo, escova, tinturas, sobrancelhas e outros). O 2º piso da loja é dividido em 03 salas onde são desenvolvidas as atividades de bem estar (massagem, estética corporal e facial, depilação e podologia) A entrar no salão de beleza o cliente se encaminha à recepção onde é realizado o pedido e encaminhamento ao profissional que fará o serviço. Finalizado o serviço o cliente retorna à recepção para realizar o pagamento. A priori, recepção será o lugar a qual pensamos colocar o cardápio para que fique visível e desde o momento da chegada do cliente não haja dúvida sobre os preços praticados "

```html
<!DOCTYPE html>
<html lang="pt-BR">
<head>
<meta charset="utf-8">
<title>Casa Aurora – Cardápio de Serviços</title>
<link rel="stylesheet" href="https://fonts.googleapis.com/css2?family=Montserrat:wght@400;500;600&family=Great+Vibes&display=swap">
<style>
  :root {
    --page-bg: #e9e9e7;
    --card-bg: #2a2c2f;
    --gold: #c9a24a;
    --gold-light: #e8c878;
    --gold-deep: #8a6a25;
    --text-light: #d9d9d6;
    --text-muted: #9c9c98;
  }
  * { box-sizing: border-box; margin: 0; padding: 0; }
  html, body {
    width: 1200px; height: 1200px; overflow: hidden;
    background: var(--page-bg);
    font-family: "Montserrat", Arial, sans-serif;
  }
  .menu-card {
    position: absolute; left: 230px; top: 45px;
    width: 740px; height: 1110px;
    background: var(--card-bg);
    overflow: hidden;
    box-shadow: 0 6px 24px rgba(0,0,0,.18);
  }
  .brand {
    position: absolute; right: 70px; top: 58px;
    text-align: right;
  }
  .brand-name {
    font-weight: 600; font-size: 40px; letter-spacing: 4px;
    color: var(--gold); text-transform: uppercase;
  }
  .brand-tagline {
    font-size: 12px; color: var(--text-muted); letter-spacing: 3px;
    text-transform: uppercase; margin-top: 2px;
  }
  .menu-title {
    font-family: "Great Vibes", cursive;
    font-weight: 400;
    font-size: 52px; color: var(--gold); margin-top: 14px;
  }
  .service-list {
    position: absolute; left: 60px; right: 60px; top: 225px;
    list-style: none;
  }
  .service {
    display: flex; align-items: flex-end; justify-content: space-between;
    gap: 24px;
    padding: 9px 0 10px;
    border-bottom: 1px solid rgba(201,162,74,.15);
  }
  .service-info { max-width: 500px; }
  .service-name {
    font-weight: 600; font-size: 15px; letter-spacing: 1px;
    color: var(--gold); text-transform: uppercase;
  }
  .service-desc {
    font-size: 13px; line-height: 1.4; color: var(--text-light); margin-top: 3px;
  }
  .service-price {
    font-weight: 500; font-size: 14px; color: var(--text-light); white-space: nowrap;
  }
  .contact {
    position: absolute; left: 60px; bottom: 52px;
    list-style: none;
  }
  .contact-item {
    display: flex; align-items: center; gap: 10px;
    font-size: 13px; color: var(--text-light); margin-top: 8px;
  }
  .contact-item svg { width: 16px; height: 16px; flex: none; }
  .gold-ornament-area {
    position: absolute; right: 0; bottom: 0;
    width: 400px; height: 150px;
    background: linear-gradient(160deg, rgba(201,162,74,0) 0%, rgba(138,106,37,.55) 45%, rgba(232,200,120,.8) 100%);
  }
</style>
</head>
<body>
  <main class="menu-card">
    <header class="brand">
      <div class="brand-name">Casa Aurora</div>
      <div class="brand-tagline">salão e bem-estar</div>
      <h1 class="menu-title">Cardápio</h1>
    </header>

    <ul class="service-list">
      <li class="service"><div class="service-info"><div class="service-name">Corte Feminino</div><div class="service-desc">Lavagem, corte personalizado e finalização com escova modeladora.</div></div><div class="service-price">R$ 00,00</div></li>
      <li class="service"><div class="service-info"><div class="service-name">Corte Masculino</div><div class="service-desc">Corte na tesoura ou máquina com acabamento e lavagem inclusos.</div></div><div class="service-price">R$ 00,00</div></li>
      <li class="service"><div class="service-info"><div class="service-name">Escova Modeladora</div><div class="service-desc">Escova lisa ou com volume, de acordo com o comprimento dos fios.</div></div><div class="service-price">R$ 00,00</div></li>
      <li class="service"><div class="service-info"><div class="service-name">Tintura</div><div class="service-desc">Coloração completa com produtos de qualidade e tratamento final.</div></div><div class="service-price">R$ 00,00</div></li>
      <li class="service"><div class="service-info"><div class="service-name">Manicure e Pedicure</div><div class="service-desc">Cuidado completo das unhas com esmaltação tradicional ou em gel.</div></div><div class="service-price">R$ 00,00</div></li>
      <li class="service"><div class="service-info"><div class="service-name">Design de Sobrancelhas</div><div class="service-desc">Modelagem com pinça ou linha respeitando o formato do rosto.</div></div><div class="service-price">R$ 00,00</div></li>
      <li class="service"><div class="service-info"><div class="service-name">Massagem Relaxante</div><div class="service-desc">Sessão de sessenta minutos com óleos aromáticos e música suave.</div></div><div class="service-price">R$ 00,00</div></li>
      <li class="service"><div class="service-info"><div class="service-name">Limpeza de Pele</div><div class="service-desc">Higienização profunda, extração e hidratação facial personalizada.</div></div><div class="service-price">R$ 00,00</div></li>
      <li class="service"><div class="service-info"><div class="service-name">Depilação</div><div class="service-desc">Depilação com cera morna ou fria em diversas áreas do corpo.</div></div><div class="service-price">R$ 00,00</div></li>
      <li class="service"><div class="service-info"><div class="service-name">Podologia</div><div class="service-desc">Tratamento dos pés com cuidado das unhas e remoção de calosidades.</div></div><div class="service-price">R$ 00,00</div></li>
    </ul>

    <ul class="contact">
      <li class="contact-item">
        <svg viewBox="0 0 24 24" fill="var(--gold)"><path d="M6.6 10.8a15.1 15.1 0 0 0 6.6 6.6l2.2-2.2c.3-.3.7-.4 1-.2 1.1.4 2.3.6 3.6.6.6 0 1 .4 1 1V20c0 .6-.4 1-1 1A17 17 0 0 1 3 4c0-.6.4-1 1-1h3.5c.6 0 1 .4 1 1 0 1.3.2 2.5.6 3.6.1.3 0 .7-.2 1z"/></svg>
        (11) 4000-1234
      </li>
      <li class="contact-item">
        <svg viewBox="0 0 24 24" fill="var(--gold)"><path d="M12 2a7 7 0 0 0-7 7c0 5.2 7 13 7 13s7-7.8 7-13a7 7 0 0 0-7-7zm0 9.5a2.5 2.5 0 1 1 0-5 2.5 2.5 0 0 1 0 5z"/></svg>
        Rua das Acácias, 250 – Centro
      </li>
      <li class="contact-item">
        <svg viewBox="0 0 24 24" fill="none" stroke="var(--gold)" stroke-width="2"><circle cx="12" cy="12" r="9"/><path d="M3 12h18M12 3c3 3.5 3 14.5 0 18M12 3c-3 3.5-3 14.5 0 18"/></svg>
        casaaurora.com.br
      </li>
    </ul>

    <div class="gold-ornament-area" role="img" aria-label="Ornamento decorativo dourado no canto inferior do cardápio"></div>
  </main>
</body>
</html>
```